Wendell's UPDATE -Across the Board

Insurance Agent Business card and probably everything else !
Been in business for over 35 years and never took the time to update so really like the black-gold combo but open for suggestions (Honestly, I have NO idea how this works but sounds very cool ) Attached are two samples that I enjoy. The black and gold option is my favorite so looking for something like that!

```html
<!DOCTYPE html>
<html lang="en">
<head>
<meta charset="UTF-8">
<title>WSH Business Card</title>
<link href="https://fonts.googleapis.com/css2?family=Libre+Baskerville:wght@700&family=Montserrat:wght@400;500&display=swap" rel="stylesheet">
<style>
  :root {
    --backdrop: #1c1c1c;
    --card: #1a1a1a;
    --card-edge: #262626;
    --gold: #c9a04a;
    --gold-soft: #b48c3c;
  }
  * { margin: 0; padding: 0; box-sizing: border-box; }
  html, body {
    width: 1200px;
    height: 900px;
    overflow: hidden;
    background: var(--backdrop);
  }
  .stage {
    width: 1200px;
    height: 900px;
    display: flex;
    flex-direction: column;
    align-items: center;
    justify-content: center;
    gap: 40px;
  }
  .card {
    position: relative;
    width: 640px;
    height: 366px;
    background: linear-gradient(135deg, var(--card) 0%, var(--card-edge) 100%);
    box-shadow: 0 18px 40px rgba(0, 0, 0, 0.55);
  }
  .card--front {
    display: flex;
    align-items: center;
    justify-content: center;
  }
  .brand-name {
    font-family: "Libre Baskerville", Georgia, serif;
    font-weight: 700;
    color: var(--gold);
    letter-spacing: 0.22em;
  }
  .card--front .brand-name {
    font-size: 44px;
    margin-left: 0.22em;
  }
  .card--back .brand-name {
    position: absolute;
    left: 56px;
    top: 40px;
    font-size: 64px;
  }
  .contact {
    position: absolute;
    left: 56px;
    top: 132px;
    color: var(--gold);
    font-family: "Montserrat", Arial, sans-serif;
  }
  .contact__name {
    font-family: "Libre Baskerville", Georgia, serif;
    font-weight: 700;
    font-size: 20px;
    letter-spacing: 0.03em;
  }
  .contact__role, .contact__est {
    font-size: 15px;
    line-height: 1.3;
    color: var(--gold-soft);
  }
  .contact__address {
    margin-top: 12px;
    font-size: 15px;
    line-height: 1.35;
    font-style: normal;
  }
  .contact__lines {
    margin-top: 12px;
    list-style: none;
    font-size: 15px;
    line-height: 1.45;
  }
  .contact__lines li {
    display: flex;
    align-items: center;
    gap: 8px;
  }
  .contact__lines svg {
    width: 13px;
    height: 13px;
    flex-shrink: 0;
  }
  .mark-frame {
    position: absolute;
    right: 70px;
    top: 110px;
    width: 180px;
    height: 180px;
    border: 1.5px solid var(--gold);
  }
</style>
</head>
<body>
  <main class="stage">
    <section class="card card--front">
      <span class="brand-name">WSH</span>
    </section>

    <section class="card card--back">
      <span class="brand-name">WSH</span>
      <div class="contact">
        <p class="contact__name">WENDELL S HALVORSEN</p>
        <p class="contact__role">Insurance &amp; Financial Consultant</p>
        <p class="contact__est">Est. 1985</p>
        <address class="contact__address">
          4120 Palm Crest Avenue,<br>
          Suite 210-3 Coral Harbor,<br>
          FL 33190
        </address>
        <ul class="contact__lines">
          <li>
            <svg viewBox="0 0 16 16" fill="none" stroke="currentColor" stroke-width="1.5" aria-hidden="true">
              <path d="M4 2 L6 2 L7 5 L5.5 6.5 C6.5 8.5 7.5 9.5 9.5 10.5 L11 9 L14 10 L14 12 C14 13 13 14 12 14 C7 14 2 9 2 4 C2 3 3 2 4 2 Z"/>
            </svg>
            954-555-0142
          </li>
          <li>
            <svg viewBox="0 0 16 16" fill="none" stroke="currentColor" stroke-width="1.5" aria-hidden="true">
              <rect x="4" y="1.5" width="8" height="13" rx="1.5"/>
              <line x1="7" y1="12" x2="9" y2="12"/>
            </svg>
            954-555-0187
          </li>
          <li>
            <svg viewBox="0 0 16 16" fill="none" stroke="currentColor" stroke-width="1.5" aria-hidden="true">
              <rect x="1.5" y="3.5" width="13" height="9"/>
              <polyline points="1.5,3.5 8,9 14.5,3.5"/>
            </svg>
            wendell@wshinsures.com
          </li>
        </ul>
      </div>
      <div class="mark-frame" aria-hidden="true"></div>
    </section>
  </main>
</body>
</html>
```